Harbourline Metro Business Racquet Circuit (est.1952)

The Metro Business Racquet Circuit began in 1952 and has been played every year since. It is the longest running continuous sporting competition in the Sydney CBD. It is a team squash competition from May to Oct yearly played between companies, sporting groups or just a groups of friends.
We are looking for a flyer that we can reuse every year (so the content within the flyer can't be tied to a specific time). Other specific we are looking for are
1. Squash imagery (can either be real or graphic design) depicting action / athleticism / friendly rivalry
2. Needs the following content
a ) "A Sydney CBD based competition for friendly rivalry between companies, sporting clubs or between friends"
b) "All matches in and around the CBD from 5.30pm to 8pm"
c) "We cater for all playing abilities"
d) "Ladies beginner comp includes complimentary coaching"
e) "Visit our website www.plvqn.org.au for more info or contact Walter on frontw@qmx.com.au"

Flyer needs to include the logos attached in file upload section

```html
<!DOCTYPE html>
<html lang="en">
<head>
<meta charset="utf-8">
<title>Harbourline Metro Business Racquet Circuit</title>
<link href="https://fonts.googleapis.com/css2?family=Anton&family=Archivo+Black&family=Oswald:wght@600;700&family=Raleway:wght@300;700&family=Roboto+Condensed:wght@400&display=swap" rel="stylesheet">
<style>
  :root {
    --sky: #b9f1fb;
    --paper: #ffffff;
    --title-orange: #f07a1c;
    --title-pink: #d4237a;
    --promo-orange: #e8620f;
    --promo-red: #b3121b;
    --teal-dark: #3a7fa6;
    --teal: #3eaab7;
    --ink: #111111;
    --alert-red: #d0121e;
    --link-blue: #2f6f99;
    --navy: #14224a;
    --gold: #c9a24a;
    --player-blue: #1f86d6;
  }
  * { margin: 0; padding: 0; box-sizing: border-box; }
  html, body { width: 816px; height: 1200px; overflow: hidden; background: var(--paper); }
  .flyer {
    position: relative;
    width: 816px; height: 1200px;
    overflow: hidden;
    background: linear-gradient(180deg, var(--sky) 0%, var(--sky) 72%, #e4fafd 86%, var(--paper) 100%);
    text-align: center;
  }
  .flyer__title {
    position: absolute; top: 50px; left: 0; right: 0;
    font-family: "Anton", sans-serif;
    font-size: 57px; line-height: 48px;
    letter-spacing: -1.5px;
    color: var(--title-orange);
    -webkit-text-stroke: 3px var(--title-pink);
    paint-order: stroke fill;
  }
  .flyer__title .line2 { color: var(--title-pink); -webkit-text-stroke: 3px #fff; }
  .hero {
    position: absolute; top: 150px; left: 40px; width: 740px; height: 360px;
  }
  .hero__art { position: absolute; inset: 0; width: 100%; height: 100%; }
  .hero__mark {
    position: absolute; left: 50%; top: 170px; transform: translateX(-50%);
    display: flex; align-items: center; gap: 10px;
    font-family: "Oswald", sans-serif; font-weight: 700; font-size: 30px;
    color: var(--navy); white-space: nowrap;
  }
  .hero__mark .dot { width: 22px; height: 22px; border-radius: 50%; background: var(--navy); }
  .promo {
    position: absolute; top: 510px; left: 0; right: 0;
    font-family: "Archivo Black", sans-serif;
    font-size: 37px; line-height: 35px; letter-spacing: -0.5px;
    color: var(--promo-orange);
    -webkit-text-stroke: 2px #fff;
    paint-order: stroke fill;
  }
  .promo .deep { color: var(--promo-red); }
  .venue {
    position: absolute; top: 686px; left: 0; right: 0;
    font-family: "Oswald", sans-serif; font-weight: 700;
    font-size: 61px; line-height: 54px; letter-spacing: -1.5px;
    text-shadow: 0 0 6px #fff;
  }
  .venue span { display: block; }
  .venue .l1 { color: var(--teal-dark); }
  .venue .l2 { color: #3a8fae; }
  .venue .l3 { color: var(--teal); }
  .abilities {
    position: absolute; top: 864px; left: 0; right: 0;
    font-family: "Archivo Black", sans-serif; font-size: 28.5px; color: var(--ink);
    letter-spacing: -0.6px;
  }
  .coaching {
    position: absolute; top: 906px; left: 0; right: 0;
    font-family: "Roboto Condensed", sans-serif; font-size: 37px; line-height: 30px;
    color: var(--alert-red); letter-spacing: -2.4px;
  }
  .contact {
    position: absolute; top: 978px; left: 0; right: 0;
    font-family: "Raleway", sans-serif; font-weight: 300;
    font-size: 31px; line-height: 30px; letter-spacing: -1.2px;
    color: var(--link-blue);
  }
  .contact strong { font-weight: 700; }
  .partners {
    position: absolute; top: 1074px; left: 56px; right: 52px; height: 86px;
    display: flex; align-items: center; justify-content: space-between;
  }
  .partner {
    display: flex; align-items: center; gap: 8px;
    font-family: "Oswald", sans-serif; font-weight: 600; font-size: 22px;
    color: var(--navy); white-space: nowrap; line-height: 1.05; text-align: left;
  }
  .partner .sq { width: 66px; height: 66px; border-radius: 50%; background: #5fb8d6; flex: none; }
  .partner--tiny { font-size: 16px; letter-spacing: 1px; }
  .partner--small { font-size: 19px; letter-spacing: 0.5px; }
  .badge { width: 84px; height: 84px; border-radius: 50%; background: var(--navy); border: 5px solid var(--gold); }
</style>
</head>
<body>
<main class="flyer">
  <h1 class="flyer__title">HARBOURLINE METRO BUSINESS<br><span class="line2">RACQUET CIRCUIT</span></h1>

  <section class="hero">
    <svg class="hero__art" viewBox="0 0 740 360" preserveAspectRatio="none" role="img" aria-label="Illustration of two squash players lunging toward each other mid-swing, with bursts of blue, pink and dark abstract swirls behind them">
      <defs>
        <radialGradient id="glow" cx="50%" cy="55%" r="55%">
          <stop offset="0" stop-color="#ffffff"/>
          <stop offset="0.5" stop-color="#e6f9fc"/>
          <stop offset="1" stop-color="#b9f1fb" stop-opacity="0"/>
        </radialGradient>
        <radialGradient id="leftPlayer" cx="30%" cy="45%" r="30%">
          <stop offset="0" stop-color="#1f86d6"/>
          <stop offset="0.5" stop-color="#2a5f9e" stop-opacity="0.8"/>
          <stop offset="1" stop-color="#2a5f9e" stop-opacity="0"/>
        </radialGradient>
        <radialGradient id="rightPlayer" cx="70%" cy="45%" r="30%">
          <stop offset="0" stop-color="#1f86d6"/>
          <stop offset="0.5" stop-color="#2a5f9e" stop-opacity="0.8"/>
          <stop offset="1" stop-color="#2a5f9e" stop-opacity="0"/>
        </radialGradient>
        <radialGradient id="pinkBurst" cx="58%" cy="25%" r="22%">
          <stop offset="0" stop-color="#e0297f"/>
          <stop offset="1" stop-color="#e0297f" stop-opacity="0"/>
        </radialGradient>
        <radialGradient id="darkBurst" cx="42%" cy="20%" r="20%">
          <stop offset="0" stop-color="#2b2b33" stop-opacity="0.7"/>
          <stop offset="1" stop-color="#2b2b33" stop-opacity="0"/>
        </radialGradient>
        <radialGradient id="warmFloor" cx="35%" cy="85%" r="25%">
          <stop offset="0" stop-color="#f0895a" stop-opacity="0.7"/>
          <stop offset="1" stop-color="#f0895a" stop-opacity="0"/>
        </radialGradient>
      </defs>
      <rect width="740" height="360" fill="url(#glow)"/>
      <rect width="740" height="360" fill="url(#darkBurst)"/>
      <rect width="740" height="360" fill="url(#pinkBurst)"/>
      <rect width="740" height="360" fill="url(#warmFloor)"/>
      <rect width="740" height="360" fill="url(#leftPlayer)"/>
      <rect width="740" height="360" fill="url(#rightPlayer)"/>
      <circle cx="370" cy="190" r="82" fill="#ffffff" opacity="0.85"/>
    </svg>
    <div class="hero__mark"><span class="dot"></span>Metro Racquet</div>
  </section>

  <p class="promo">
    A SYDNEY CBD COMPETITION<br>
    PROMOTING FRIENDLY RIVALRY<br>
    BETWEEN COMPANIES,<br>
    <span class="deep">SPORTING CLUBS<br>AND MATES</span>
  </p>

  <p class="venue">
    <span class="l1">ALL MATCHES</span>
    <span class="l2">IN AND AROUND THE CBD</span>
    <span class="l3">FROM 5.30PM TO 8PM</span>
  </p>

  <p class="abilities">WE CATER FOR ALL PLAYING ABILITIES</p>

  <p class="coaching">LADIES BEGINNER COMP INCLUDES<br>COMPLIMENTARY COACHING</p>

  <p class="contact">
    Visit our website <strong>www.plvqn.org.au for more info</strong><br>
    or contact Walter on <strong>frontw@qmx.com.au</strong>
  </p>

  <footer class="partners">
    <div class="partner"><span class="sq"></span>Bayside Racquet<br>Academy</div>
    <div class="partner partner--tiny">PLVQN</div>
    <div class="partner partner--small">PLOVER LANE RACQUET ASSOCIATION</div>
    <div class="badge" role="img" aria-label="Partner club anniversary badge"></div>
  </footer>
</main>
</body>
</html>
```